Home decoration company - sustainable wall panels

- I would need you to design 5-10 pages for my client's website.
- The design should have details of wall panels that are being sold on the website - lomaverdesigns.com.
- It should have wood + sustainability branding.
- please focus on using shapes of products that are being sold on the website and use them as design for branding

See more here
https://sheets.pinvale.net/d/7qrTbXwe2KmPzUaLdNcVfYhGjRsOiEtyBnMuWxA/edit

Target Market(s)

people who are want sustainable home/business wall decor

Industry/Entity Type

Interior Decoration

Logo Text

Lomaver Designs (for favicon, "LD")

Number of Pages Required

5+ page

Font styles to use
Serif
Sans Serif

Requirements
Must have
• - details of products that are being sold on the website lomaverdesigns.com (you will see there are different wall panel shapes)
- great creative design ideas
- follow instructions from here https://sheets.pinvale.net/d/7qrTbXwe2KmPzUaLdNcVfYhGjRsOiEtyBnMuWxA/edit
- the design must be at least 2 levels above the current one on lomaverdesigns.com
- use photos from here https://files.pinvale.net/folders/4kWzMbQeRtYuIoPa8SdFgH-jKl
Nice to have
• - it would be nice if you would give your own creative suggestions
Should not have
• - should not look like it's a 1990s website

```html
<!DOCTYPE html>
<html lang="en">
<head>
<meta charset="utf-8">
<title>Lomaver Designs – Wood Panels With a Story</title>
<link href="https://fonts.googleapis.com/css2?family=Roboto:ital,wght@0,400;0,500;0,700;1,400&display=swap" rel="stylesheet">
<style>
:root{
  --periwinkle:#8796c0;
  --ink:#222;
  --text:#555;
  --muted:#777;
  --paper:#efedeb;
  --paper-2:#e6e3df;
  --white:#fff;
  --footer:#2b2b31;
  --footer-text:#cfd0d6;
  --gold:#e0a93a;
}
*{box-sizing:border-box;margin:0;padding:0}
html,body{width:1200px;height:5013px;overflow:hidden}
body{font-family:'Roboto',Arial,sans-serif;color:var(--text);position:relative;background:linear-gradient(180deg,var(--paper),var(--paper-2) 50%,var(--paper));}
a{color:inherit;text-decoration:none}

/* top bar */
.topbar{position:absolute;top:0;left:0;width:1200px;height:40px;background:var(--periwinkle);color:#fff;font-size:12px;display:flex;align-items:center;padding:0 111px;}
.topbar u{font-weight:700}
.topbar .contacts{margin-left:auto;display:flex;gap:28px;align-items:center}
.topbar .contacts span{display:flex;align-items:center;gap:6px}

/* nav */
.nav{position:absolute;top:40px;left:0;width:1200px;height:87px;background:var(--white);display:flex;align-items:center;padding:0 111px;}
.brand{font-size:25px;font-weight:500;color:var(--ink)}
.menu{margin-left:auto;display:flex;gap:22px;font-size:13px;font-weight:500;color:var(--ink)}
.menu .active{color:var(--periwinkle);border-bottom:2px solid var(--periwinkle);padding-bottom:6px}

/* hero */
.hero{position:absolute;top:127px;left:0;width:1200px;height:600px;background:linear-gradient(160deg,#2a1a10 0%,#6b4020 40%,#9a6535 60%,#3b2414 100%);}
.hero h1{position:absolute;left:111px;top:185px;color:#fff;font-size:33px;font-weight:500}
.hero .sub{position:absolute;left:111px;top:236px;color:#fff;font-size:20px}
.btn{position:absolute;height:46px;border-radius:23px;font-size:15px;font-weight:700;display:flex;align-items:center;justify-content:center;gap:8px}
.btn-shop{left:111px;top:302px;width:200px;background:var(--periwinkle);color:#fff}
.btn-bulk{left:336px;top:302px;width:200px;background:#fff;color:var(--ink)}
.hero .note{position:absolute;left:111px;top:370px;width:510px;color:#fff;font-size:12px;font-style:italic;line-height:22px}
.arrow-btn{position:absolute;width:34px;height:34px;border-radius:50%;border:2px solid #fff;display:flex;align-items:center;justify-content:center}

/* certificates */
.section-title{position:absolute;left:0;width:1200px;text-align:center;color:var(--ink);font-size:33px;font-weight:500;line-height:42px}
.cert-row{position:absolute;top:910px;left:116px;display:flex;gap:30px}
.cert{width:170px;height:88px;background:#fff;display:flex;align-items:center;justify-content:center}
.cert-shape{width:56px;height:56px;border-radius:50%}
.small-arrow{position:absolute;top:940px;width:30px;height:30px;border-radius:50%;background:#fff;display:flex;align-items:center;justify-content:center;box-shadow:0 1px 3px rgba(0,0,0,.2)}
.cert-text{position:absolute;top:1030px;left:170px;width:860px;text-align:center;font-size:14px;line-height:27px;color:var(--muted)}

/* feature cards */
.card{position:absolute;top:1230px;width:310px;height:373px;background:#fff;box-shadow:0 2px 6px rgba(0,0,0,.08);text-align:center}
.card .photo{height:198px}
.card h3{margin-top:34px;font-size:18px;font-weight:500;color:var(--ink)}
.card p{margin:14px 22px 0;font-size:14px;line-height:22px;color:var(--muted)}

/* origin */
.origin{position:absolute;top:1826px;width:284px;text-align:center}
.circle{width:284px;height:284px;border-radius:50%;border:3px solid var(--periwinkle);padding:6px;background:#fff}
.circle div{width:100%;height:100%;border-radius:50%}
.origin h3{margin-top:22px;font-size:19px;font-weight:700;color:var(--ink)}
.origin p{margin-top:12px;font-size:14px;line-height:21px;color:var(--muted)}

/* reviews */
.reviews{position:absolute;top:2358px;left:0;width:1200px;height:504px;background:var(--periwinkle);color:#fff}
.reviews h2{position:absolute;top:56px;width:1200px;text-align:center;font-size:33px;font-weight:500;letter-spacing:.5px}
.review{position:absolute;top:120px;width:300px}
.quote{font-size:46px;font-weight:700;line-height:46px;height:46px}
.review p{font-size:12px;font-style:italic;line-height:26px}
.review p b{font-style:normal;text-decoration:underline;font-weight:700}
.reviewer{display:flex;align-items:center;gap:8px;margin-top:10px;font-size:11px}
.avatar{width:34px;height:34px;border-radius:50%;background:linear-gradient(135deg,#b57744,#5b3a20);flex:none}
.stars{color:var(--gold);font-size:9px;letter-spacing:1px}
.badge-shape{position:absolute;left:470px;top:312px;width:90px;height:90px;border-radius:50%;background:#b8773d}
.btn-now{left:600px;top:345px;width:134px;height:38px;border-radius:19px;background:#fff;color:var(--ink);font-size:14px}
.reviews .note{position:absolute;top:424px;width:1200px;text-align:center;font-size:11px;font-style:italic}

/* products */
.prod-img{position:absolute;width:490px;height:363px}
.prod-icon{position:absolute;left:572px;width:56px;height:56px;border-radius:50%;background:var(--periwinkle);border:3px solid #fff;box-shadow:0 0 0 2px var(--periwinkle);display:flex;align-items:center;justify-content:center}
.prod-text{position:absolute;width:430px}
.prod-text h2{font-size:33px;font-weight:500;color:var(--ink);margin-bottom:22px}
.prod-text p{font-size:14px;line-height:25px;color:var(--muted);margin-bottom:14px}
.learn{display:flex;align-items:center;gap:6px;font-size:13px;font-weight:700;color:var(--periwinkle);margin-top:20px}

/* footer */
.footer{position:absolute;top:4590px;left:0;width:1200px;height:423px;background:var(--footer);color:var(--footer-text)}
.footer h4{position:absolute;font-size:15px;font-weight:700;color:#fff}
.footer .brand{position:absolute;left:111px;top:100px;color:#fff;font-size:30px}
.social{position:absolute;left:150px;top:152px;display:flex;gap:6px}
.social span{width:34px;height:34px;border-radius:50%;border:2px solid #fff}
.flinks{position:absolute;left:363px;top:92px;font-size:12px;line-height:24px;color:#fff}
.fcontact{position:absolute;left:508px;display:flex;gap:16px;font-size:12px;color:#fff;line-height:17px}
.fcontact .ic{width:38px;height:38px;border-radius:50%;border:2px solid #fff;display:flex;align-items:center;justify-content:center;flex:none}
.field{position:absolute;left:783px;width:305px;background:#fff;color:#555;font-size:11px;padding:8px 10px;border:1px solid #ccc}
.submit{position:absolute;left:783px;top:285px;width:96px;height:32px;border-radius:16px;background:var(--periwinkle);color:#fff;font-size:13px;font-weight:700;display:flex;align-items:center;justify-content:center}
.fbadges{position:absolute;top:250px;left:111px;display:flex;gap:60px;align-items:center}
.fbadge{width:72px;height:72px;border-radius:50%;background:#3c3c44;border:2px solid #6a6a74}
.fbadge.sq{border-radius:6px}
.copy{position:absolute;top:385px;width:1200px;text-align:center;font-size:12px;color:#fff}
</style>
</head>
<body>

<div class="topbar">
  <span>Ordering larger quantities? <u>Call us.</u></span>
  <div class="contacts">
    <span><svg width="11" height="11" viewBox="0 0 24 24"><path fill="#fff" d="M6.6 10.8a15 15 0 006.6 6.6l2.2-2.2c.3-.3.7-.4 1-.2 1.1.4 2.3.6 3.6.6.6 0 1 .4 1 1V20c0 .6-.4 1-1 1A17 17 0 013 4c0-.6.4-1 1-1h3.5c.6 0 1 .4 1 1 0 1.3.2 2.5.6 3.6.1.3 0 .7-.2 1z"/></svg>Phone +1 555 014 2273</span>
    <span>Email us: <svg width="12" height="10" viewBox="0 0 24 18"><rect x="1" y="1" width="22" height="16" fill="#fff"/><path d="M1 1l11 9 11-9" stroke="#8796c0" stroke-width="2" fill="none"/></svg>hello@lomaverstudio.com</span>
    <span><svg width="12" height="10" viewBox="0 0 24 18"><rect x="1" y="1" width="22" height="16" fill="#fff"/><path d="M1 1l11 9 11-9" stroke="#8796c0" stroke-width="2" fill="none"/></svg>orders@lomaverpanels.net</span>
  </div>
</div>

<header class="nav">
  <div class="brand">Lomaver Designs</div>
  <nav class="menu">
    <a class="active">HOME</a><a>WALL PANELING</a><a>DOORS</a><a>CUTTING BOARDS</a><a>TABLE TOPS</a><a>ABOUT US</a><a>CONTACT US</a>
  </nav>
</header>

<section class="hero" role="img" aria-label="Restaurant interior with reclaimed teak wall panels, wooden tables and stools">
  <h1>Wood Panels With a Story</h1>
  <div class="sub">100% Sustainable. 100% Hand Crafted. 100% Unique.</div>
  <a class="btn btn-shop">SHOP AT HOMEVALE <svg width="14" height="14" viewBox="0 0 16 16"><circle cx="8" cy="8" r="8" fill="#fff"/><path d="M6 4l4 4-4 4" stroke="#8796c0" stroke-width="2" fill="none"/></svg></a>
  <a class="btn btn-bulk">BULK ORDER <svg width="14" height="14" viewBox="0 0 16 16"><circle cx="8" cy="8" r="8" fill="#222"/><path d="M6 4l4 4-4 4" stroke="#fff" stroke-width="2" fill="none"/></svg></a>
  <div class="note">* our products have a 10 year warranty: Each purchase backed by a limited 10 year warranty for residential applications.</div>
  <div class="arrow-btn" style="left:36px;top:283px"><svg width="12" height="12" viewBox="0 0 12 12"><path d="M8 1L3 6l5 5" stroke="#fff" stroke-width="2" fill="none"/></svg></div>
  <div class="arrow-btn" style="left:1128px;top:283px"><svg width="12" height="12" viewBox="0 0 12 12"><path d="M4 1l5 5-5 5" stroke="#fff" stroke-width="2" fill="none"/></svg></div>
</section>

<h2 class="section-title" style="top:790px">Key certificates that we use for the<br>Plywood substrate</h2>
<div class="small-arrow" style="left:43px"><svg width="10" height="10" viewBox="0 0 10 10"><path d="M7 0L2 5l5 5z" fill="#333"/></svg></div>
<div class="cert-row">
  <div class="cert"><div class="cert-shape" style="background:#5aa043"></div></div>
  <div class="cert"><div class="cert-shape" style="border-radius:4px;background:#2f7a45"></div></div>
  <div class="cert"><div class="cert-shape" style="border-radius:4px;background:#ddd;width:70px;height:40px"></div></div>
  <div class="cert"><div class="cert-shape" style="background:#d7def0;border:3px solid #5a6fb0"></div></div>
  <div class="cert"><div class="cert-shape" style="border-radius:4px;background:#222;width:70px;height:44px"></div></div>
</div>
<div class="small-arrow" style="left:1126px"><svg width="10" height="10" viewBox="0 0 10 10"><path d="M3 0l5 5-5 5z" fill="#333"/></svg></div>
<p class="cert-text">As a wood-based industry, company demonstrate its performance in sustainable production forest management and timber legality verification, that complies with the criteria and indicator according to Regulation of Director General of Forestry Business Development. Surveillance once a year.</p>

<article class="card" style="left:111px"><div class="photo" role="img" aria-label="Lit wall of multicoloured reclaimed wood panels" style="background:linear-gradient(120deg,#3a2a1e,#8a5f3c 45%,#a9733f 60%,#2d241d)"></div><h3>Sustainable</h3><p>Lorem ipsum dolor sit amet, consectetur adipiscing elit, sed do eiusmod tempor incididunt ut labore et</p></article>
<article class="card" style="left:445px"><div class="photo" role="img" aria-label="Close-up of weathered carved reclaimed boat wood" style="background:linear-gradient(180deg,#9c8a7c,#c6b6a6 50%,#8e7a6b)"></div><h3>Hand Crafted</h3><p>Lorem ipsum dolor sit amet, consectetur adipiscing elit, sed do eiusmod tempor incididunt ut labore et</p></article>
<article class="card" style="left:779px"><div class="photo" role="img" aria-label="Reclaimed wood panel wall above a modern fireplace" style="background:linear-gradient(135deg,#e9e6e2,#7a4a2a 45%,#3a2418 70%,#d0ccc8)"></div><h3>Unique</h3><p>Lorem ipsum dolor sit amet, consectetur adipiscing elit, sed do eiusmod tempor incididunt ut labore et</p></article>

<h2 class="section-title" style="top:1743px">Lomaver Designs Wall Panel Origin Story</h2>
<div class="origin" style="left:111px"><div class="circle"><div role="img" aria-label="Old fishermen's boats on a beach" style="background:linear-gradient(180deg,#b9c6d6,#8d8a7e 55%,#6b5a48)"></div></div><h3>Reclaim</h3><p>We search the shores of East Java for teakwood fishermen's boats and barns which are no longer usable and transform them into gorgeous and durable décor for your home or business.</p></div>
<div class="origin" style="left:455px"><div class="circle"><div role="img" aria-label="Craftsmen sorting and cutting reclaimed wood in a workshop" style="background:linear-gradient(160deg,#3f3a34,#7a5a3e 50%,#2e2a26)"></div></div><h3>Recycle</h3><p>Each of these unique boats or pieces is painstakingly dismantled by master craftsmen. The wood is then dried for 8-12 months to ensure exceptional durability.</p></div>
<div class="origin" style="left:803px"><div class="circle"><div role="img" aria-label="Finished multicoloured wall panel installed indoors" style="background:linear-gradient(120deg,#2a2420,#6e5a4a 40%,#a8763f 70%,#3a2e25)"></div></div><h3>Create</h3><p>Every panel is unique given they are expertly handmade using different combinations of boat pieces and reclaimed</p></div>

<section class="reviews">
  <h2>VERIFIED REVIEWS FOR OUR PRODUCTS</h2>
  <div class="review" style="left:111px"><div class="quote">&ldquo;</div><p>After looking at so many options to create an accent wall behind our TV, we found this amazing product! Easy to install (just need a <b>READ MORE</b></p><div class="reviewer"><span class="avatar"></span><div>MARCUS FROM RIDGEFIELD, MN<div class="stars">★★★★★</div></div></div></div>
  <div class="review" style="left:453px"><div class="quote">&ldquo;</div><p>Exactly what we were looking for. Brushed a little lemon oil to brighten up the natural wood. Homevale customer service was excellent. <b>READ MORE</b></p><div class="reviewer"><span class="avatar"></span><div>LENA FROM CORAL BAY, SC<div class="stars">★★★★★</div></div></div></div>
  <div class="review" style="left:795px"><div class="quote">&ldquo;</div><p>The panels had a very good look to them. The wood color variations within the panels weren't as distinct as much as the picture <b>READ MORE</b></p><div class="reviewer"><span class="avatar"></span><div>TESSA FROM SD<div class="stars">★★★★★</div></div></div></div>
  <div class="badge-shape"></div>
  <a class="btn btn-now">SHOP NOW</a>
  <div class="note">* our products have a 10 year warranty: Each purchase backed by a limited 10 year warranty for residential applications.</div>
</section>

<div class="prod-img" style="left:111px;top:2980px;background:linear-gradient(120deg,#e8d2bd,#c79a74 35%,#7a4e34 65%,#5a6a52)" role="img" aria-label="Bedroom with a reclaimed wood panel accent wall"></div>
<div class="prod-icon" style="top:3143px"><svg width="24" height="24" viewBox="0 0 24 24" fill="none" stroke="#fff" stroke-width="1.6"><rect x="3" y="3" width="18" height="18"/><path d="M3 9h18M9 9v12M15 9v12"/></svg></div>
<div class="prod-text" style="left:666px;top:3015px"><h2>Wall Panels</h2><p>We search the shores of East Java for teak fishermen's boats and barns which are no longer usable and transform them into panels. This also provides local fisherman a sustainable income. Every panel is unique given they are expertly handmade using different combinations of boat pieces and reclaimed wood.</p><p>Quality is our top priority. All our products undergo rigorous inspection before packaging.</p><a class="learn">LEARN MORE <svg width="12" height="12" viewBox="0 0 16 16"><circle cx="8" cy="8" r="8" fill="#8796c0"/><path d="M6 4l4 4-4 4" stroke="#fff" stroke-width="2" fill="none"/></svg></a></div>

<div class="prod-img" style="left:600px;top:3343px;background:linear-gradient(100deg,#3a3a3c,#b58f62 30%,#8d6a46 55%,#c9a273 75%,#3f3f42)" role="img" aria-label="Row of reclaimed wood mosaic doors leaning against a wall"></div>
<div class="prod-icon" style="top:3497px"><svg width="24" height="24" viewBox="0 0 24 24" fill="none" stroke="#fff" stroke-width="1.6"><rect x="6" y="2" width="12" height="20"/><circle cx="15" cy="12" r="1"/></svg></div>
<div class="prod-text" style="left:111px;top:3405px"><h2>Doors</h2><p>Lorem ipsum dolor sit amet, consectetur adipiscing elit, sed do eiusmod tempor incididunt ut labore et dolore magna aliqua. Ut enim ad minim veniam, quis nostrud exercitation ullamco laboris nisi ut aliquip ex ea commodo consequat. Duis aute irure dolor in reprehenderit in voluptate velit esse</p><a class="learn">LEARN MORE <svg width="12" height="12" viewBox="0 0 16 16"><circle cx="8" cy="8" r="8" fill="#8796c0"/><path d="M6 4l4 4-4 4" stroke="#fff" stroke-width="2" fill="none"/></svg></a></div>

<div class="prod-img" style="left:111px;top:3706px;background:linear-gradient(135deg,#d8d8d6,#c7c5c1 40%,#9b6a3e 55%,#d4d2ce 80%)" role="img" aria-label="Wooden cutting board with bread and avocado"></div>
<div class="prod-icon" style="top:3860px"><svg width="24" height="24" viewBox="0 0 24 24" fill="none" stroke="#fff" stroke-width="1.6"><rect x="6" y="5" width="12" height="17" rx="2"/><path d="M10 2h4v3h-4z"/></svg></div>
<div class="prod-text" style="left:666px;top:3780px"><h2>Cutting boards</h2><p>Our boards are made out of reclaimed teak by local villagers. Each is finished with a food grade antibacterial coating that also helps maintain both the strength and the flexibility of the wood fibers. Each board is also water repellent, preventing oxidation and decay.</p><a class="learn">LEARN MORE <svg width="12" height="12" viewBox="0 0 16 16"><circle cx="8" cy="8" r="8" fill="#8796c0"/><path d="M6 4l4 4-4 4" stroke="#fff" stroke-width="2" fill="none"/></svg></a></div>

<div class="prod-img" style="left:600px;top:4069px;background:linear-gradient(160deg,#5a3a22,#8c5a30 40%,#c08a4a 55%,#3a2616)" role="img" aria-label="Reclaimed teak table top in a wood-panelled room"></div>
<div class="prod-icon" style="top:4227px"><svg width="24" height="24" viewBox="0 0 24 24" fill="none" stroke="#fff" stroke-width="1.6"><rect x="3" y="6" width="18" height="5"/><path d="M6 11v9M18 11v9M6 15h12"/></svg></div>
<div class="prod-text" style="left:111px;top:4130px"><h2>Table tops</h2><p>Our table tops are made out of reclaimed teak by local villagers. Each is finished with a food grade antibacterial coating that also helps maintain both the strength and the flexibility of the wood fibers. Each table top is also water repellent, preventing oxidation and decay.</p><a class="learn">LEARN MORE <svg width="12" height="12" viewBox="0 0 16 16"><circle cx="8" cy="8" r="8" fill="#8796c0"/><path d="M6 4l4 4-4 4" stroke="#fff" stroke-width="2" fill="none"/></svg></a></div>

<footer class="footer">
  <div class="brand">Lomaver Designs</div>
  <div class="social"><span></span><span></span><span></span></div>
  <h4 style="left:363px;top:62px">Company</h4>
  <div class="flinks">Home<br>Wall Panels<br>Doors<br>Cutting Boards<br>About Us</div>
  <h4 style="left:508px;top:62px">Contact Us</h4>
  <div class="fcontact" style="top:100px"><span class="ic"><svg width="16" height="16" viewBox="0 0 24 24"><path fill="#fff" d="M6.6 10.8a15 15 0 006.6 6.6l2.2-2.2c.3-.3.7-.4 1-.2 1.1.4 2.3.6 3.6.6.6 0 1 .4 1 1V20c0 .6-.4 1-1 1A17 17 0 013 4c0-.6.4-1 1-1h3.5c.6 0 1 .4 1 1 0 1.3.2 2.5.6 3.6.1.3 0 .7-.2 1z"/></svg></span><div><b>phone number</b><br>+1 555 014 2273</div></div>
  <div class="fcontact" style="top:150px"><span class="ic"><svg width="16" height="12" viewBox="0 0 24 18"><rect x="1" y="1" width="22" height="16" fill="#fff"/><path d="M1 1l11 9 11-9" stroke="#2b2b31" stroke-width="2" fill="none"/></svg></span><div><b>Email us</b><br>hello@lomaverstudio.com<br>orders@lomaverpanels.net</div></div>
  <h4 style="left:783px;top:62px">Get In Touch:</h4>
  <div class="field" style="top:100px;height:30px">Name:</div>
  <div class="field" style="top:142px;height:30px">Email :</div>
  <div class="field" style="top:184px;height:82px">Message :</div>
  <div class="submit">SUBMIT</div>
  <div class="fbadges"><span class="fbadge"></span><span class="fbadge sq"></span><span class="fbadge"></span><span class="fbadge sq"></span><span class="fbadge"></span></div>
  <div class="copy">Copyrights © 2020, lomaverdesigns.com. All Rights Reserved. &nbsp;|&nbsp; Privacy policy</div>
</footer>

</body>
</html>
```